依頼詳細
コーポレートカラーがオレンジなので、オレンジをベースにデザインをお願いしたいと思っております。
見やすさ、内容の伝わりやすさ、先進的なイメージを与えつつ、信頼できる雰囲気のチラシデザインだと嬉しいです。
イメージ画像や写真などは独自にご提案いただいて構いません。
よろしくお願い致します。
記載項目
素案のファイルを添付します
サイズ
A4
ページ数
両面
希望イメージ
シンプル 複雑
単色 カラフル
暗い 明るい
日常 高級
遊び心 厳粛
未来的 伝統的
女性的 男性的
希望する色
黄・オレンジ系
納品ファイル
• 高解像度JPG (.jpg)
• イラストレーター形式 (.ai)
• フォトショップ形式 (.psd)
• PNG形式 (.png)
補足説明

伝わりやすいデザインで、独自のキャッチコピー提案がありました。裏面も見やすい形でデザインしていただけてとてもよかったです。ありがとうございました。

この度はお忙しい中、ご提案いただきましてありがとうございました。
また機会がございましたら、ご提案いただけますと幸いです。

```html
<!DOCTYPE html>
<html lang="ja">
<head>
<meta charset="utf-8">
<title>AI 業務自動化ソリューション</title>
<link rel="stylesheet" href="https://fonts.googleapis.com/css2?family=Noto+Sans+JP:wght@400;500;700;900&family=Montserrat:wght@400;500&display=swap">
<style>
:root{
  --red:#d8261c;
  --orange:#ef7d12;
  --orange-deep:#c94f0a;
  --orange-light:#f7a23a;
  --dark:#1d1f24;
  --ink:#2a2a2a;
  --white:#ffffff;
}
*{margin:0;padding:0;box-sizing:border-box}
html,body{width:849px;height:1200px;overflow:hidden;background:#fff}
body{font-family:"Noto Sans JP",sans-serif;color:var(--ink)}
.flyer{position:relative;width:849px;height:1200px;overflow:hidden;background:#fff}

.hero-photo{position:absolute;right:0;top:0;width:430px;height:470px;
  background:radial-gradient(circle at 55% 40%,#f4b25a 0%,#b7581a 28%,#3a2a22 62%,#1a1b20 100%);}
.hero-fade{position:absolute;left:419px;top:0;width:120px;height:470px;background:linear-gradient(90deg,#fff,rgba(255,255,255,0))}

.title{position:absolute;left:40px;top:18px;font-weight:900;line-height:1;
  background:linear-gradient(180deg,var(--red),var(--orange));-webkit-background-clip:text;background-clip:text;color:transparent}
.title .ai{display:block;font-size:120px;letter-spacing:4px}
.title .line{display:block;font-size:66px;margin-top:14px;letter-spacing:2px}

.intro-band{position:absolute;left:0;top:0;width:849px;height:1200px}
.intro-text{position:absolute;left:40px;top:440px;width:400px;color:var(--white);font-size:15px;line-height:1.75;font-weight:500}
.brand{position:absolute;left:560px;top:482px;display:flex;align-items:center;gap:12px;
  font-family:"Montserrat",sans-serif;font-size:42px;font-weight:400;color:var(--white);letter-spacing:1px}
.brand .dot{width:14px;height:14px;background:var(--orange-light)}

.section-title{position:absolute;left:40px;top:608px;color:var(--white);font-weight:900;font-size:50px;letter-spacing:2px}
.section-rule{position:absolute;left:40px;top:680px;width:240px;height:4px;background:var(--white)}

.video-photo{position:absolute;left:40px;top:705px;width:215px;height:140px;
  background:linear-gradient(135deg,#3b4656,#7a8aa0 55%,#2a3240)}
.video-caption{position:absolute;left:270px;top:745px;width:140px;color:var(--white);font-size:15px;line-height:1.6;font-weight:500}

.point{position:absolute;left:40px;width:260px}
.point-tag{display:block;width:110px;margin:0 auto -10px;background:var(--red);color:var(--white);
  text-align:center;font-family:"Montserrat",sans-serif;font-weight:500;font-size:16px;letter-spacing:2px;padding:4px 0;position:relative;z-index:1}
.point-body{background:var(--white);padding:20px 16px 14px;font-size:13px;line-height:1.6;color:var(--ink)}

.feature{position:absolute;border-radius:50%;background:var(--white);text-align:center;display:flex;flex-direction:column;align-items:center;padding-top:28px}
.feature h3{color:var(--red);font-weight:900;font-size:26px;line-height:1.25;margin-top:6px}
.feature p{font-size:11px;line-height:1.55;color:var(--ink);margin-top:8px;width:62%}
</style>
</head>
<body>
<div class="flyer">
  <div class="hero-photo" role="img" aria-label="Hand touching a glowing digital interface, orange technology imagery"></div>
  <div class="hero-fade"></div>

  <h1 class="title">
    <span class="ai">AI</span>
    <span class="line">業務自動化</span>
    <span class="line">ソリューション</span>
  </h1>

  <svg class="intro-band" viewBox="0 0 849 1200" aria-hidden="true">
    <defs>
      <linearGradient id="orangeField" x1="0" y1="0" x2="0" y2="1">
        <stop offset="0" stop-color="#f28a1c"/>
        <stop offset="1" stop-color="#d9620e"/>
      </linearGradient>
    </defs>
    <polygon points="0,575 849,520 849,1200 0,1200" fill="url(#orangeField)"/>
    <polygon points="0,420 849,395 849,540 0,590" fill="#1d1f24"/>
    <polygon points="0,590 849,540 849,548 0,598" fill="#f7a23a"/>
  </svg>

  <p class="intro-text">AIによって業務を効率化・自動化し、<br>お客さまのパフォーマンス最大化を支援します。<br>最適なデバイスの選定、ソフト・ハードの設置、<br>テスト、PDCAサイクルまで、<br>トータルに導入をサポートします。</p>

  <div class="brand"><span class="dot"></span>Novalyne</div>

  <h2 class="section-title">AI動画解析</h2>
  <div class="section-rule"></div>

  <div class="video-photo" role="img" aria-label="Operator monitoring multiple video analysis screens"></div>
  <p class="video-caption">ヒト・モノ・コトの特徴をリアルタイムに検出</p>

  <div class="point" style="top:865px">
    <span class="point-tag">POINT</span>
    <div class="point-body">人物の属性情報の取得、製造・物流現場での不良品の検出、危険エリアへの侵入検知</div>
  </div>
  <div class="point" style="top:990px">
    <span class="point-tag">POINT</span>
    <div class="point-body">人の目に頼っていた作業の自動化や、業務効率化、安全対策の支援を可能にします。</div>
  </div>

  <div class="feature" style="left:440px;top:655px;width:260px;height:260px">
    <svg width="44" height="40" viewBox="0 0 44 40" aria-hidden="true">
      <rect x="4" y="26" width="7" height="12" fill="#d8261c"/>
      <rect x="15" y="20" width="7" height="18" fill="#d8261c"/>
      <rect x="26" y="13" width="7" height="25" fill="#d8261c"/>
      <path d="M4 18 L20 8 L28 12 L40 3" stroke="#d8261c" stroke-width="3" fill="none"/>
    </svg>
    <h3>業務効率化<br>支援</h3>
    <p>自動化すべき業務の現状をしっかりと把握し、最適な提案をご提示。プロセス全体の効率を向上します。</p>
  </div>

  <div class="feature" style="left:300px;top:905px;width:255px;height:255px">
    <svg width="40" height="40" viewBox="0 0 40 40" aria-hidden="true">
      <circle cx="16" cy="16" r="11" stroke="#d8261c" stroke-width="4" fill="none"/>
      <path d="M24 24 L37 37" stroke="#d8261c" stroke-width="5" stroke-linecap="round"/>
    </svg>
    <h3>高精度の<br>認識率</h3>
    <p>AI画像認識とハイパラ最適化の学習を組み合わせることにより、高精度の認識を実現します。</p>
  </div>

  <div class="feature" style="left:570px;top:900px;width:250px;height:250px;padding-top:40px">
    <svg width="40" height="40" viewBox="0 0 40 40" aria-hidden="true">
      <circle cx="20" cy="20" r="17" stroke="#d8261c" stroke-width="3.5" fill="none"/>
      <rect x="18" y="9" width="4" height="15" fill="#d8261c"/>
      <rect x="18" y="27" width="4" height="4" fill="#d8261c"/>
    </svg>
    <h3>解析＋アルファ</h3>
    <p>解析するだけでなく、データの可視化や分析、デバイスへの連携等、柔軟に対応します。</p>
  </div>
</div>
</body>
</html>
```